Summer Sale Graphics for Social Media

I want to create 11 social media graphics (new Instagram size 4:5 (1080 x 1350 pixels) focusing on our Summer Sale Graphics, using any of the pics attached. Use the attached pics, NO RANDOM STOCK PHOTOGRAPHY. For the color scheme of the graphics, they should all be complementary to the product colors in the photos.
You can add any of the photos attached but none are required. You can do some of the graphics in all text. I mainly need BOLD text that says one of the headlines (11 total) SEE ATTACHED WORD DOCUMENT for the headlines to use.

```html
<!DOCTYPE html>
<html lang="en">
<head>
<meta charset="utf-8">
<title>Summer Sale Social Graphics</title>
<link rel="stylesheet" href="https://fonts.googleapis.com/css2?family=Oswald:wght@500;600;700&family=Montserrat:wght@700&display=swap">
<style>
  :root {
    --board: #1a1a1a;
    --card: #ffffff;
    --magenta: #c2399b;
    --blue: #3a62ae;
    --shade: #3b1f4f;
    --deco-teal: #bfeee4;
    --deco-violet: #c9cdf7;
  }
  html, body {
    margin: 0;
    padding: 0;
    width: 1200px;
    height: 1200px;
    overflow: hidden;
    background: var(--board);
  }
  .board {
    position: relative;
    width: 1200px;
    height: 1200px;
  }
  .card {
    position: absolute;
    width: 288px;
    height: 360px;
    background: var(--card);
    overflow: hidden;
  }
  .deco {
    position: absolute;
    left: 0;
    top: 0;
    width: 172px;
    height: 118px;
    background:
      radial-gradient(circle at 45% 45%, var(--deco-violet) 0%, rgba(201,205,247,0) 55%),
      linear-gradient(135deg, var(--deco-teal) 0%, rgba(255,255,255,0) 85%);
  }
  .ln {
    position: absolute;
    left: 0;
    right: 0;
    margin: 0;
    display: flex;
    justify-content: center;
    transform: translateY(-50%);
    line-height: 1;
    font-family: "Oswald", sans-serif;
    font-weight: 600;
    text-transform: uppercase;
    white-space: nowrap;
    letter-spacing: -0.3px;
  }
  .ln span {
    display: inline-block;
    flex: none;
    transform: scaleX(0.82);
    background: linear-gradient(90deg, var(--magenta) 0%, var(--blue) 100%);
    -webkit-background-clip: text;
    background-clip: text;
    color: transparent;
  }
  .ln.big {
    font-weight: 700;
  }
  .ln.big span {
    filter: drop-shadow(2px 2px 0 var(--shade));
  }
  .offer {
    position: absolute;
    left: 50%;
    transform: translate(-50%, -50%);
    width: 119px;
    height: 28px;
    border-radius: 6px;
    background: var(--magenta);
    color: #fff;
    font-family: "Montserrat", sans-serif;
    font-weight: 700;
    font-size: 13px;
    line-height: 28px;
    text-align: center;
    white-space: nowrap;
  }
</style>
</head>
<body>
<main class="board">

  <section class="card" style="left:11px; top:14px;">
    <div class="deco" role="img" aria-label="Geometric summer pattern of triangles, chevrons and dots"></div>
    <p class="ln" style="top:170px; font-size:22px;"><span>Your summer body won't wait</span></p>
    <p class="ln big" style="top:206px; font-size:45px;"><span>Sale now!</span></p>
    <div class="offer" style="top:264px;">Up to $15 OFF</div>
  </section>

  <section class="card" style="left:309px; top:14px;">
    <div class="deco" role="img" aria-label="Geometric summer pattern of triangles, chevrons and dots"></div>
    <p class="ln" style="top:170px; font-size:22px;"><span>Final countdown to summer</span></p>
    <p class="ln big" style="top:206px; font-size:45px;"><span>Sale now!</span></p>
    <div class="offer" style="top:264px;">Up to $15 OFF</div>
  </section>

  <section class="card" style="left:609px; top:14px;">
    <div class="deco" role="img" aria-label="Geometric summer pattern of triangles, chevrons and dots"></div>
    <p class="ln" style="top:140px; font-size:21px;"><span>Detox, burn fat,</span></p>
    <p class="ln" style="top:166px; font-size:21px;"><span>and turn heads this summer</span></p>
    <p class="ln big" style="top:206px; font-size:45px;"><span>Sale now!</span></p>
    <div class="offer" style="top:264px;">Up to $15 OFF</div>
  </section>

  <section class="card" style="left:908px; top:14px;">
    <div class="deco" role="img" aria-label="Geometric summer pattern of triangles, chevrons and dots"></div>
    <p class="ln" style="top:150px; font-size:37px;"><span>Summer's here.</span></p>
    <p class="ln" style="top:197px; font-size:21px;"><span>And we're having the biggest</span></p>
    <p class="ln" style="top:228px; font-size:38px;"><span>Sale of the year</span></p>
    <div class="offer" style="top:280px;">Up to $15 OFF</div>
  </section>

  <section class="card" style="left:11px; top:389px;">
    <div class="deco" role="img" aria-label="Geometric summer pattern of triangles, chevrons and dots"></div>
    <p class="ln" style="top:173px; font-size:36px;"><span>One sale. One body.</span></p>
    <p class="ln" style="top:211px; font-size:27px;"><span>One summer to slay</span></p>
    <div class="offer" style="top:259px;">Up to $15 OFF</div>
  </section>

  <section class="card" style="left:309px; top:389px;">
    <div class="deco" role="img" aria-label="Geometric summer pattern of triangles, chevrons and dots"></div>
    <p class="ln" style="top:146px; font-size:29px;"><span>Summer isn't waiting</span></p>
    <p class="ln" style="top:177px; font-size:29px;"><span>Neither should you</span></p>
    <p class="ln big" style="top:222px; font-size:45px;"><span>Sale now!</span></p>
    <div class="offer" style="top:272px;">Up to $15 OFF</div>
  </section>

  <section class="card" style="left:609px; top:389px;">
    <div class="deco" role="img" aria-label="Geometric summer pattern of triangles, chevrons and dots"></div>
    <p class="ln" style="top:111px; font-size:29px;"><span>Slim waist.</span></p>
    <p class="ln" style="top:142px; font-size:29px;"><span>Flat tummy.</span></p>
    <p class="ln" style="top:173px; font-size:29px;"><span>More energy.</span></p>
    <p class="ln big" style="top:214px; font-size:44px;"><span>Let's go!</span></p>
    <p class="ln big" style="top:259px; font-size:52px;"><span>Sale now</span></p>
    <div class="offer" style="top:308px;">Up to $15 OFF</div>
  </section>

  <section class="card" style="left:908px; top:389px;">
    <div class="deco" role="img" aria-label="Geometric summer pattern of triangles, chevrons and dots"></div>
    <p class="ln big" style="top:130px; font-size:40px;"><span>Hurry!</span></p>
    <p class="ln" style="top:176px; font-size:32px;"><span>Our summer</span></p>
    <p class="ln" style="top:209px; font-size:29px;"><span>Slim-down sale is on</span></p>
    <p class="ln" style="top:256px; font-size:44px;"><span>Don't miss it!</span></p>
    <div class="offer" style="top:306px;">Up to $15 OFF</div>
  </section>

  <section class="card" style="left:159px; top:765px;">
    <div class="deco" role="img" aria-label="Geometric summer pattern of triangles, chevrons and dots"></div>
    <p class="ln big" style="top:154px; font-size:58px;"><span>Sale</span></p>
    <p class="ln" style="top:211px; font-size:31px;"><span>Your summer body</span></p>
    <p class="ln" style="top:241px; font-size:31px;"><span>starts here</span></p>
    <div class="offer" style="top:292px;">Up to $15 OFF</div>
  </section>

  <section class="card" style="left:457px; top:765px;">
    <div class="deco" role="img" aria-label="Geometric summer pattern of triangles, chevrons and dots"></div>
    <p class="ln big" style="top:135px; font-size:56px;"><span>Limited</span></p>
    <p class="ln" style="top:187px; font-size:32px;"><span>Time summer sale</span></p>
    <p class="ln" style="top:222px; font-size:29px;"><span>Snatch your</span></p>
    <p class="ln" style="top:253px; font-size:29px;"><span>supplements now!</span></p>
    <div class="offer" style="top:294px;">Up to $15 OFF</div>
  </section>

  <section class="card" style="left:761px; top:765px;">
    <div class="deco" role="img" aria-label="Geometric summer pattern of triangles, chevrons and dots"></div>
    <p class="ln" style="top:133px; font-size:32px;"><span>Get snatched for</span></p>
    <p class="ln big" style="top:177px; font-size:56px;"><span>Summer</span></p>
    <p class="ln" style="top:223px; font-size:29px;"><span>Supplements</span></p>
    <p class="ln" style="top:255px; font-size:35px;"><span>On sale now!</span></p>
    <div class="offer" style="top:299px;">Up to $15 OFF</div>
  </section>

</main>
</body>
</html>
```